Car rental website design for a UAE car rental company

This project is about creating a new website design for a car rental company located in Dubai (United Arab Emirates), I opened the same project a few months ago but I didn't receive a lot of appealing entries so I closed it but this time I am marking the project as guaranteed to avoid such situation again, if you have already provided a design before then please re-submit again on this project so that it is considered while reviewing all the designs

A few important things:

1- We need a simple non-complex design
2- The final deliverable would be 2 screens (PSD, JPEG ... etc), the first screen is for the home page and the second screen is for an internal page
3- The home page must have a section that end users can use to rent a car online directly from the home page instead of going into some inner pages
4- The current website is very old and not very appealing so avoid creating a similar design (www.quarvin-drive.example)
5- The name is Quarvin but the company rents normal cars (no Limousin cars will be rented) so avoid adding any fancy cars in the images/graphics used in the design, just normal end users cars
6- The expected pages would be: home, About us, Our team, Strategy, Contact us and links to social media pages
7- The attachments include the company's logo and some screens from other car rental companies that provide online rentals/payments

If you have any questions please feel free to ask and please note that we will need the designs urgently

Thanks

Target Market(s)

Dubai - United Arab Emirates

Industry/Entity Type

It Company

Number of Pages Required

2 page

Font styles to use
Sans Serif

Requirements
Must have
• Check the project details
Nice to have
Should not have

```html
<!DOCTYPE html>
<html lang="en">
<head>
<meta charset="utf-8">
<title>Quarvin Rent A Car</title>
<link href="https://fonts.googleapis.com/css2?family=Figtree:wght@400;600;700&display=swap" rel="stylesheet">
<style>
:root{
  --maroon:#7a1233;
  --maroon-dark:#3d0718;
  --hero-top:#2a0612;
  --hero-mid:#5a0f26;
  --hero-low:#8a1a33;
  --ink:#1a1a1a;
  --muted:#7b7b7b;
  --line:#d6d6d6;
  --yellow:#ffd21f;
  --footer:#353535;
  --footer-text:#b5b5b5;
  --white:#ffffff;
}
*{box-sizing:border-box;margin:0;padding:0}
html,body{width:1152px;height:1200px;overflow:hidden;background:var(--white)}
body{font-family:"Figtree",sans-serif;color:var(--ink);position:relative}
.abs{position:absolute}

/* hero */
.hero{position:absolute;left:0;top:0;width:1152px;height:476px;
  background:radial-gradient(ellipse 700px 380px at 820px 330px,var(--hero-low),transparent 70%),
  linear-gradient(180deg,var(--hero-top) 0%,var(--hero-mid) 60%,#6e1530 100%);
  box-shadow:0 3px 6px rgba(0,0,0,.35)}
.brand{left:82px;top:10px;width:112px;text-align:center}
.brand-mark{display:block;width:32px;height:32px;margin:0 auto 6px;background:var(--white);border:2px solid #c8c8c8}
.brand-name{font-size:17px;font-weight:600;color:#d9d9d9;line-height:1}
.call{left:236px;top:37px;color:var(--yellow);font-size:16px;font-weight:600}
.divider-v{width:1px;height:18px;background:rgba(255,255,255,.25)}
.nav{left:596px;top:37px;display:flex;gap:0;font-size:16px;color:var(--white)}
.nav a{color:inherit;text-decoration:none;padding:0 14px;border-left:1px solid rgba(255,255,255,.25)}
.nav a:first-child{border-left:none}
.header-line{left:82px;top:82px;width:980px;height:1px;background:linear-gradient(90deg,transparent,rgba(255,255,255,.3),transparent)}

.booking{left:146px;top:115px;width:327px}
.tabs{display:flex;gap:2px;height:20px}
.tab{background:var(--maroon);color:var(--white);font-size:9px;line-height:20px;padding:0 10px;border-radius:3px 3px 0 0}
.tab:first-child{padding:0 17px}
.panel{position:relative;height:258px;background:linear-gradient(180deg,#f2f2f2,#d2d2d2 55%,#8e8e8e);border-radius:0 0 5px 5px;box-shadow:0 2px 6px rgba(0,0,0,.5);font-size:11px;color:#333}
.panel .abs{position:absolute}
.field{background:var(--white);border:1px solid #ccc;border-radius:2px;height:19px;font-size:8px;color:#999;line-height:17px;padding-left:4px}
.small{font-size:8.5px}
.panel-line{left:8px;top:190px;width:311px;height:1px;background:rgba(0,0,0,.1)}
.btn{display:inline-block;background:linear-gradient(180deg,#7c1634,#3a0616);color:var(--white);font-weight:700;font-size:12px;text-align:center;box-shadow:0 2px 3px rgba(0,0,0,.4);border:1px solid rgba(255,255,255,.2)}

.hero-title{left:510px;top:113px;font-size:28px;font-weight:700;color:var(--white)}
.hero-sub{left:510px;top:155px;width:370px;font-size:15px;line-height:21px;color:#eee}
.hero-btn{left:511px;top:215px;width:122px;line-height:33px}
.hero-car{left:617px;top:214px;width:395px;height:226px;border-radius:40% 40% 20% 20%;background:radial-gradient(ellipse at 50% 45%,#e8343b,#a8141c 60%,rgba(60,0,10,0) 78%)}
.arrow{width:32px;height:32px;border-radius:50%}
.arrow-dark{background:rgba(140,40,70,.55)}

/* content */
.h-section{font-size:28px;color:var(--maroon);font-weight:400;letter-spacing:.2px}
.rule{height:1px;background:var(--line)}
.lead{font-size:15px;color:var(--muted)}
.body{font-size:15px;line-height:21px}
.promo{left:80px;top:656px;width:487px;height:164px;background:linear-gradient(90deg,#eeeeee,#d9d9d9);border-radius:2px}
.promo-title{left:18px;top:18px;font-size:20px;line-height:23px;color:#222}
.promo-text{left:17px;top:80px;width:190px;font-size:15px;line-height:21px;color:#444}
.promo-img{left:280px;top:656px;width:272px;height:184px;border-radius:30% 30% 15% 15%;background:radial-gradient(ellipse at 50% 55%,#cfcfcf,#9a9a9a 55%,rgba(200,200,200,0) 75%)}
.tag{left:468px;top:676px;width:78px;height:62px;background:#c8102e;transform:rotate(18deg);border-radius:3px}
.mission-title{left:586px;top:652px;font-size:20px;color:#222}
.mission-text{left:586px;width:470px;font-size:15px;line-height:21px;color:#333}

.car-img{height:111px;border-radius:35% 35% 15% 15%}
.car-blue{left:136px;top:963px;width:226px;background:radial-gradient(ellipse at 50% 50%,#2d6fe0,#1240a8 55%,rgba(255,255,255,0) 75%)}
.car-red{left:601px;top:963px;width:222px;background:radial-gradient(ellipse at 50% 50%,#d4293a,#9c1322 55%,rgba(255,255,255,0) 75%)}
.model{font-size:20px;color:var(--maroon)}
.spec{font-size:14px;color:#222}
.price-label{font-size:20px;color:var(--maroon)}
.price{font-size:22px;color:#111}
.card-btn{width:121px;line-height:34px}
.arrow-light{background:var(--white);box-shadow:0 1px 4px rgba(0,0,0,.3)}

.footer{left:0;top:1137px;width:1152px;height:55px;background:var(--footer)}
.footer-bottom{left:0;top:1192px;width:1152px;height:8px;background:#111}
.footer-text{font-size:12px;color:var(--footer-text)}
.social{display:flex;gap:9px}
.social span{width:27px;height:27px;border-radius:50%;background:#5d5d5d}
</style>
</head>
<body>

<header class="hero">
  <div class="abs brand"><span class="brand-mark"></span><span class="brand-name">Quarvin</span></div>
  <div class="abs divider-v" style="left:219px;top:40px"></div>
  <div class="abs call">Call Us : +971 50 555 0142</div>
  <nav class="abs nav"><a>Home</a><a>About Us</a><a>Our Team</a><a>Strategy</a><a>Contact Us</a></nav>
  <div class="abs header-line"></div>

  <section class="abs booking">
    <div class="tabs"><span class="tab">Reservation</span><span class="tab">View / Modify / Cancel</span><span class="tab">Get A Receipt</span></div>
    <div class="panel">
      <div class="abs" style="left:8px;top:8px">Reserve your Quarvin Rent a car</div>
      <div class="abs small" style="left:76px;top:27px">Pick-up</div>
      <div class="abs" style="left:7px;top:55px">Location</div>
      <div class="abs field" style="left:75px;top:47px;width:242px">Airport, City, Zip, Address, Attraction</div>
      <div class="abs" style="left:79px;top:73px;width:10px;height:10px;background:#fff;border:1px solid #9a1b3a"></div>
      <div class="abs small" style="left:97px;top:73px">Returning to different location</div>
      <div class="abs small" style="left:76px;top:105px">Pick-up date and time</div>
      <div class="abs small" style="left:197px;top:105px">Return date time</div>
      <div class="abs" style="left:7px;top:128px">Date/Time</div>
      <div class="abs field" style="left:75px;top:122px;width:62px">mm/dd/yy</div>
      <div class="abs field" style="left:144px;top:122px;width:50px">noon</div>
      <div class="abs field" style="left:198px;top:122px;width:62px">mm/dd/yy</div>
      <div class="abs field" style="left:267px;top:122px;width:50px">noon</div>
      <div class="abs" style="left:7px;top:166px">Age/Residence</div>
      <div class="abs field" style="left:95px;top:159px;width:63px">25 yrs +</div>
      <div class="abs" style="left:165px;top:166px">Resident of</div>
      <div class="abs field" style="left:233px;top:159px;width:63px">UAE</div>
      <div class="abs panel-line"></div>
      <span class="abs btn" style="left:189px;top:210px;width:121px;line-height:33px">SELECT A CAR</span>
    </div>
  </section>

  <h1 class="abs hero-title">Rent a car in a few seconds.</h1>
  <p class="abs hero-sub">Enjoy special discount this season with exclusive savings for our customers.</p>
  <span class="abs btn hero-btn">MORE INFO</span>
  <div class="abs hero-car" role="img" aria-label="Photo of a red compact hatchback"></div>

  <svg class="abs arrow arrow-dark" style="left:81px;top:241px" viewBox="0 0 32 32"><path d="M19 10l-7 6 7 6z" fill="#3a0616"/></svg>
  <svg class="abs arrow arrow-dark" style="left:1038px;top:241px" viewBox="0 0 32 32"><path d="M13 10l7 6-7 6z" fill="#3a0616"/></svg>
</header>

<h2 class="abs h-section" style="left:81px;top:494px">WELCOME TO QUARVIN</h2>
<div class="abs rule" style="left:81px;top:537px;width:989px"></div>
<p class="abs lead" style="left:81px;top:550px">As Dubai is expected to welcome millions of tourists and visitors, car rental industry is believed to escalate more rapidly in the region.</p>
<p class="abs body" style="left:81px;top:591px;width:990px">Over the past five years, demands for car rentals in Dubai has been augmenting at a healthy pace and is currently registering a growth rate of 20 to 25 percent per year.</p>

<section class="abs promo">
  <div class="abs promo-title">DUBAI TO<br>ABU DHABI AED 200</div>
  <div class="abs promo-text">Drive across UAE for a low minimum fee.Enjoy our best price!</div>
</section>
<div class="abs promo-img" role="img" aria-label="Photo of a silver compact SUV"></div>
<div class="abs tag" role="img" aria-label="Red best price and service tag"></div>

<h3 class="abs mission-title">MISSION / VISION</h3>
<p class="abs mission-text" style="top:685px">To be one of the leading auto leasing company in the fast growing economy and tourism industry of the emirate of Dubai and play alongside with the major car rental companies in the globe.</p>
<p class="abs mission-text" style="top:762px;width:470px">Quarvin vows to deliver comfort, luxury and satisfaction to all our clients by providing them professional, hassle-free<br>and first-class service.</p>

<h2 class="abs h-section" style="left:81px;top:864px">CARS AVAILABLE</h2>
<div class="abs rule" style="left:100px;top:912px;width:950px;background:linear-gradient(90deg,transparent,#e4e4e4,transparent)"></div>

<div class="abs car-img car-blue" role="img" aria-label="Photo of a blue sedan"></div>
<div class="abs" style="left:392px;top:944px">
  <div class="model">NORVALE</div>
  <div class="spec" style="margin-top:6px">Gasoline 1.4 L, Hatchback</div>
  <div class="price-label" style="margin-top:9px">PRICE FROM:</div>
  <div class="price">AED 200 / DAY</div>
  <span class="btn card-btn" style="margin-top:14px">MORE INFO</span>
</div>

<div class="abs car-img car-red" role="img" aria-label="Photo of a red hatchback"></div>
<div class="abs" style="left:849px;top:944px">
  <div class="model">NORVALE</div>
  <div class="spec" style="margin-top:6px">Gasoline 1.4 L, Hatchback</div>
  <div class="price-label" style="margin-top:9px">PRICE FROM:</div>
  <div class="price">AED 200 / DAY</div>
  <span class="btn card-btn" style="margin-top:14px">MORE INFO</span>
</div>

<svg class="abs arrow arrow-light" style="left:81px;top:1003px" viewBox="0 0 32 32"><path d="M19 10l-7 6 7 6z" fill="#5a0b22"/></svg>
<svg class="abs arrow arrow-light" style="left:1038px;top:1003px" viewBox="0 0 32 32"><path d="M13 10l7 6-7 6z" fill="#5a0b22"/></svg>

<footer class="abs footer">
  <div class="abs footer-text" style="left:81px;top:20px">All Rights Reserved 2015 &nbsp;| &nbsp;Terms of Use &nbsp;| Privacy Policy</div>
  <div class="abs footer-text" style="left:455px;top:20px">Follow Us</div>
  <div class="abs social" style="left:523px;top:13px" aria-label="Social media links"><span></span><span></span><span></span><span></span><span></span></div>
  <div class="abs footer-text" style="right:81px;top:20px">Web Design Company</div>
</footer>
<div class="abs footer-bottom"></div>

</body>
</html>
```